UNDER ONE [BRIGHT] LANTERN, Shape your path

We are looking for a cover refresh of an existing bestselling book that is going into 3rd edition print this year.
The book is an inspirational as well as educational book that has become recognized as one of the most comprehensive, actionable, personal and financial planning resources available today for families, individuals and business owners alike.
Comprised of three true stories of loss, learning to live and love again and a 30 page checklist at the back of the book it contains tips and strategies for everyone to help them to get their personal and financial lives in order while they can.
The cover must have the following:
1. Appeal to a broad audience/both personal and corporate
2. Include Mira Tollenkamp Bestselling Author
3. Include introduction of a new Afterword
4. 3rd Edition
5. Colors to remain the same – red, black and white
6. The title must remain in caps and the word [BRIGHT] must have the brackets around it
We have also added a current copy of the second edition to help you. For your information our website is www.thetollenkampcircle.example
Reason: We have narrowed it down to our top 3 designs. We are submitting the covers to our community for them to pick the top cover. Good luck to everyone

```html
<!DOCTYPE html>
<html lang="en">
<head>
<meta charset="utf-8">
<title>Under One [Bright] Lantern – 3rd Edition Covers</title>
<link rel="stylesheet" href="https://fonts.googleapis.com/css2?family=Bebas+Neue&family=Jost:wght@400;500;700&family=Pinyon+Script&display=swap">
<style>
  :root{
    --red:#e30613;
    --red-deep:#b3121a;
    --red-mid:#cf1b22;
    --black:#0d0d0d;
    --white:#ffffff;
    --grey-dark:#4a4a4a;
  }
  *{box-sizing:border-box;margin:0;padding:0}
  html,body{width:1200px;height:849px;overflow:hidden;background:var(--white)}
  .spread{position:relative;width:1200px;height:849px}
  .cover{position:absolute;top:0;height:849px;overflow:hidden}
  .cover--photo{left:0;width:598px}
  .cover--red{left:601px;width:599px;background:radial-gradient(ellipse at 55% 45%, #d9262c 0%, var(--red-mid) 45%, var(--red-deep) 100%)}

  .photo-fill{position:absolute;inset:0;background:linear-gradient(160deg,#8a8a8a 0%,#6e6e6e 40%,var(--grey-dark) 75%,#2a2a2a 100%)}

  .title-band{position:absolute;left:0;top:296px;width:598px;height:143px;background:var(--red)}

  .display{font-family:"Bebas Neue",Impact,sans-serif;color:var(--white);white-space:nowrap;line-height:1}
  .bracket,.accent{color:var(--black)}

  .band-small{position:absolute;left:18px;top:312px;font-size:58px;line-height:1.0;transform:scaleX(.8);transform-origin:left top}
  .band-word{position:absolute;left:170px;top:298px;font-size:152px;transform:scaleX(.9);transform-origin:left top}

  .stack-small{position:absolute;left:50%;font-size:74px;transform:translateX(-50%) scaleX(.8)}
  .stack-small--top{top:34px}
  .stack-small--bottom{top:246px}
  .stack-word{position:absolute;left:50%;top:90px;font-size:190px;transform:translateX(-50%) scaleX(.86)}
  .stack-word .letter{text-shadow:5px 3px 0 rgba(0,0,0,.55)}

  .tagline{position:absolute;font-family:"Pinyon Script",cursive;color:var(--white);white-space:nowrap;transform:translateX(-50%)}
  .cover--photo .tagline{left:290px;top:528px;font-size:48px}
  .cover--red .tagline{left:281px;top:470px;font-size:58px}

  .pen-area{position:absolute;left:120px;top:340px;width:340px;height:320px;background:radial-gradient(ellipse at 50% 50%, rgba(120,10,14,.35) 0%, rgba(120,10,14,0) 70%)}

  .byline{position:absolute;left:0;right:0;text-align:center;font-family:"Jost",sans-serif;color:var(--white);text-transform:uppercase}
  .byline__role{top:731px;font-size:25px;font-weight:500;letter-spacing:.5px}
  .byline__name{top:765px;font-size:40px;font-weight:400;letter-spacing:1.5px}

  .edition-strip{position:absolute;left:0;right:0;bottom:0;height:28px;background:var(--black);text-align:center;font-family:"Jost",sans-serif;font-weight:700;font-size:19px;line-height:28px;color:var(--red);letter-spacing:.8px}
</style>
</head>
<body>
<main class="spread">

  <section class="cover cover--photo" aria-label="Cover option one">
    <div class="photo-fill" role="img" aria-label="Black and white close-up of a fountain pen nib over handwritten script"></div>
    <div class="title-band"></div>
    <h1 class="display band-small">UNDER ONE<br>LANTERN</h1>
    <p class="display band-word"><span class="bracket">[</span>BRI<span class="accent">G</span>HT<span class="bracket">]</span></p>
    <p class="tagline">Shape your path</p>
    <p class="byline byline__role">Bestselling Author</p>
    <p class="byline byline__name">Mira Tollenkamp</p>
    <p class="edition-strip">3rd EDITION - NEW AFTERWORD</p>
  </section>

  <section class="cover cover--red" aria-label="Cover option two">
    <h1 class="display stack-small stack-small--top">UNDER ONE</h1>
    <p class="display stack-word"><span class="bracket">[</span><span class="letter">BRI</span><span class="accent">G</span><span class="letter">HT</span><span class="bracket">]</span></p>
    <p class="display stack-small stack-small--bottom">LANTERN</p>
    <div class="pen-area" role="img" aria-label="Red and black fountain pen lying diagonally"></div>
    <p class="tagline">Shape your path</p>
    <p class="byline byline__role">Bestselling Author</p>
    <p class="byline byline__name">Mira Tollenkamp</p>
    <p class="edition-strip">3rd EDITION - NEW AFTERWORD</p>
  </section>

</main>
</body>
</html>
```